Dr. Lumora needs a design for its website!

*Only need the design, coding is not required.
*Need desktop version ($500) and mobile/tablet version ($200)
*The attached files are not the exact layout we want, they are just for you to know what information should be included in those pages.
*The function of our website is like www.qtv-medlist.example
*For the background picture, prefer a lively picture and chinese people in it, NOT necessarily need a doctor or sick person in the picture

***Don't just copy the layout from the attachments or from the reference website, we are looking for creative ideas, non-ordinary designs!!!****

We are developing a website for the public to search a doctor by different criteria. At the initial stage, we need 4 pages to start with and other pages at later stage. I have attached the general idea of these pages but not necessarily to be exactly the same, I am looking for some new ideas.

This website needs a professional, modern, simple and user friendly design. The main color to be used in the website will be same as the color (R:0 G:139 B:205) used in our logo (see attached). We don't have any particular thoughts for the other color and the font to be used in the website. Can try to use circle outline for the icon in the navigation bar.

1. Home: will include 4 sections (see attached)

2. Doctor's details (see attached)

3. Health information: will include a short descriptions of this Health Info page and 5 sections (see attached)

4. News (see attached)

Reason: Not too many suitable designs to choose from and need more time to go through the designs

Target Market(s)

All

Industry/Entity Type

Medical

Number of Pages Required

4 page

Requirements
Should not have
• must not be same as or looks too much like www.qtv-medlist.example
• prefer not to use black and red color

```html
<!DOCTYPE html>
<html lang="en">
<head>
<meta charset="utf-8">
<title>Health Info – Dr. Lumora</title>
<link href="https://fonts.googleapis.com/css2?family=Roboto:wght@300;400;500&display=swap" rel="stylesheet">
<style>
:root{
  --brand:#008bcd;
  --brand-dark:#0a79c2;
  --ink:#333;
  --muted:#555;
  --soft:#888;
  --line:#ddd;
  --panel-head:#f2f2f2;
  --footer:#f2f2f2;
  --ad-head:#3b5f94;
  --ad-link:#0000cc;
  --ad-url:#008000;
}
*{box-sizing:border-box;margin:0;padding:0}
html,body{width:819px;height:1200px;overflow:hidden}
body{font-family:"Roboto",Arial,sans-serif;color:var(--ink);background:#fff;position:relative;font-size:11px}
a{color:inherit;text-decoration:none}
.abs{position:absolute}

.topbar{left:0;top:0;width:819px;height:35px;background:#f0f0f0;font-size:10px;color:#444}
.topbar span{position:absolute;top:12px}
.search{left:600px;width:167px;top:10px;height:16px;border-left:1px solid #ccc;border-right:1px solid #ccc;padding-left:14px;font-style:italic;color:#888;font-size:8.5px;line-height:16px}
.header{left:0;top:35px;width:819px;height:58px;background:#fff;box-shadow:0 2px 3px rgba(0,0,0,.12)}
.brand{left:52px;top:50px;display:flex;align-items:center;gap:6px;color:var(--brand);font-size:23px;font-weight:400}
.brand i{width:30px;height:30px;border-radius:50%;background:var(--brand);display:block}
.nav span{position:absolute;top:58px;font-size:11px;color:#333;letter-spacing:.2px}
.nav .active{color:var(--brand)}

h1{left:0;width:819px;top:123px;text-align:center;font-weight:400;font-size:27px;color:#222}
h1 em{font-style:normal;color:var(--brand)}
.intro{left:90px;width:640px;top:163px;text-align:center;font-size:10px;line-height:17px;color:var(--muted)}

.panel{border:1px solid var(--line);background:#fff;overflow:hidden}
.panel-head{background:var(--panel-head);height:38px;padding:0 8px;display:flex;align-items:center;justify-content:space-between;color:var(--brand-dark);font-size:14px}
.more{background:var(--brand-dark);color:#fff;font-size:11px;font-weight:500;padding:7px 9px;display:flex;align-items:center;gap:4px}
.post{padding:5px 10px 5px;font-size:10px;line-height:16.5px;color:var(--muted)}
.post + .post{border-top:1px solid var(--line);margin:0 10px;padding:6px 0 5px}
.post .t{color:var(--brand-dark);font-size:10.5px;line-height:16px}
.post .d{color:var(--soft);line-height:15px}
.post .r{color:var(--brand-dark)}
.grid3{display:grid;grid-template-columns:72px 72px 72px;padding:1px 10px;font-size:9.5px;line-height:16.8px;color:var(--muted)}
.grid3 u{color:var(--brand-dark);font-weight:500}
.cols{display:flex;padding:4px 10px}
.cols div{width:240px;font-size:10px;line-height:17px;color:var(--muted)}
.cols h3{font-weight:400;color:var(--brand-dark);font-size:12px;margin-bottom:8px}
.cols u{display:block;margin-top:4px;color:var(--brand-dark);font-weight:500}
.tips{padding:6px 10px;font-size:10px;line-height:17px;color:var(--muted)}
.tips li{list-style:none;display:flex;gap:7px;margin-bottom:4px}
.tips li i{width:10px;height:10px;border:1.5px solid var(--brand);border-radius:50%;flex:none;margin-top:3px}
.btn{display:inline-block;background:var(--brand-dark);color:#fff;font-weight:500;font-size:11px;padding:8px 16px;margin:1px 0 0 2px}

.ad{border:1px solid var(--ad-head);font-family:Arial,sans-serif;width:213px}
.ad-head{background:var(--ad-head);color:#fff;font-size:6px;padding:1px 2px;text-decoration:underline}
.ad-item{border-top:1px solid var(--ad-head);padding:3px 2px;font-size:6.2px;line-height:8.5px;color:#000;min-height:44px}
.ad-item:first-of-type{border-top:0}
.ad-item b{color:var(--ad-link);text-decoration:underline;font-size:6.5px}
.ad-item s{text-decoration:none;color:var(--ad-url);display:block}

.footer{left:0;top:891px;width:819px;height:267px;background:var(--footer)}
.fcol{position:absolute;top:18px;font-size:10px;color:#888;line-height:21.5px}
.fcol h4{font-weight:400;color:var(--brand-dark);font-size:12px;margin-bottom:6px}
.fcol .on{color:#222}
.social span{display:flex;align-items:center;gap:10px}
.social i{width:8px;height:8px;border-radius:50%;background:#999;display:block}
.totop{left:388px;top:1085px}
.copy{left:0;top:1158px;width:819px;height:42px;background:var(--brand-dark);color:#fff;text-align:center;line-height:42px;font-size:9px;font-weight:500}
.copy em{font-style:normal;color:#9fd8f5}
</style>
</head>
<body>

<div class="abs topbar">
  <span style="left:234px">Login</span>
  <span style="left:291px">Register</span>
  <span style="left:362px">Forgot username/Password?</span>
  <span style="left:525px">Language ▾</span>
  <div class="abs search">⌕ Search Information</div>
</div>
<div class="abs header"></div>
<div class="abs brand"><i></i>Dr. Lumora</div>
<nav class="nav">
  <span class="active" style="left:295px;border-bottom:2px solid var(--brand);border-radius:0 0 20px 20px;padding:0 4px 4px">HOME</span>
  <span style="left:361px">ABOUT</span>
  <span style="left:433px">DOCTOR LIST</span>
  <span style="left:540px">HEALTH INFO</span>
  <span style="left:646px">NEWS</span>
  <span style="left:711px">CONTACT</span>
</nav>

<h1 class="abs">Health <em>Info</em></h1>
<p class="abs intro">Lorem Ipsum is simply dummy text of the printing and typesetting industry. Lorem Ipsum has been the industry's standard dummy text ever since the 1500s, when an unknown printer took a galley of type and scrambled it to make a type specimen book.</p>

<section class="abs panel" style="left:53px;top:235px;width:227px;height:195px">
  <div class="panel-head">Health Articles <span class="more">✚ MORE</span></div>
  <div class="post"><div class="t">Lorem Ipsum is simply dummy text</div><div class="d">▦ 21 September 2016</div>Lorem Ipsum is dummy text of the printing and typesetting industry...<span class="r">READ MORE</span></div>
  <div class="post"><div class="t">Lorem Ipsum is simply dummy text</div><div class="d">▦ 21 September 2016</div>Lorem Ipsum is dummy text of the printing and typesetting industry...<span class="r">READ MORE</span></div>
</section>

<section class="abs panel" style="left:302px;top:235px;width:227px;height:195px">
  <div class="panel-head">Diseases - What? Why? How?</div>
  <div class="grid3">
    <span>Lorem Ipsum</span><span>Lorem Ipsum</span><span>Lorem Ipsum</span>
    <span>Lorem Ipsum</span><span>Lorem Ipsum</span><span>Lorem Ipsum</span>
    <span>Lorem Ipsum</span><span>Lorem Ipsum</span><span>Lorem Ipsum</span>
    <span>Lorem Ipsum</span><span>Lorem Ipsum</span><span>Lorem Ipsum</span>
    <span>Lorem Ipsum</span><span>Lorem Ipsum</span><span>Lorem Ipsum</span>
    <span>Lorem Ipsum</span><span>Lorem Ipsum</span><span>Lorem Ipsum</span>
    <span>Lorem Ipsum</span><span>Lorem Ipsum</span><span>Lorem Ipsum</span>
    <span>Lorem Ipsum</span><span>Lorem Ipsum</span><span>Lorem Ipsum</span>
    <span>Lorem Ipsum</span><span>Lorem Ipsum</span><u>MORE</u>
  </div>
</section>

<section class="abs panel" style="left:53px;top:450px;width:478px;height:194px">
  <div class="panel-head">Medical Support Team (Emergency / Non-Emergency)</div>
  <div class="cols">
    <div><h3>Emergency</h3>Lorem Ipsum is dummy text of the printing<br>Lorem Ipsum is dummy text.<br>Lorem Ipsum is dummy text.<br>Lorem Ipsum is dummy text of the printing<br>Lorem Ipsum is dummy text.<u>READ MORE</u></div>
    <div><h3>Non-Emergency</h3>Lorem Ipsum is dummy text of the printing<br>Lorem Ipsum is dummy text.<br>Lorem Ipsum is dummy text.<br>Lorem Ipsum is dummy text of the printing<br>Lorem Ipsum is dummy text.<u>READ MORE</u></div>
  </div>
</section>

<section class="abs panel" style="left:53px;top:662px;width:227px;height:194px">
  <div class="panel-head">Medical Insurance Tip</div>
  <ul class="tips">
    <li><i></i>Lorem Ipsum is dummy text of the printing and typ esetting industry...</li>
    <li><i></i>Lorem Ipsum is dummy text of the printing and typ esetting industry...</li>
    <li><i></i>Lorem Ipsum is dummy text of the</li>
    <li><i></i>Lorem Ipsum is dummy text of the</li>
    <span class="btn">VIEW ALL</span>
  </ul>
</section>

<section class="abs panel" style="left:302px;top:662px;width:227px;height:194px">
  <div class="panel-head">Medical Development <span class="more">✚ MORE</span></div>
  <div class="post"><div class="t">Lorem Ipsum is simply dummy text</div><div class="d">▦ 21 September 2016</div>Lorem Ipsum is dummy text of the printing and typesetting industry...<span class="r">READ MORE</span></div>
  <div class="post"><div class="t">Lorem Ipsum is simply dummy text</div><div class="d">▦ 21 September 2016</div>Lorem Ipsum is dummy text of the printing and typesetting industry...<span class="r">READ MORE</span></div>
</section>

<aside class="abs ad" style="left:553px;top:236px">
  <div class="ad-head">Sponsored links</div>
  <div class="ad-item"><b>Starvale, Novalux, &amp; More</b><br>Premier US Starvale &amp; Novalux Dealer 25 years of friendly expert service<s>www.starvale-shop.example</s></div>
  <div class="ad-item"><b>SkyPoint scope upgrade</b><br>SV200 Classic, SkyDrive, Twinstar No software - just plug &amp; play<s>www.skypoint-eng.example</s></div>
  <div class="ad-item"><b>GPS for Starvale Telescopes</b><br>Add GPS to your SV-ET or SVX55 Scope Fully Integrated Unit - Only $169!<s>www.scopelinker.example</s></div>
  <div class="ad-item"><b>Free Telescope Catalog</b><br>Special low prices on telescopes at Polaris Optics' authoritative website<s>www.polaris-optics.example</s></div>
</aside>
<aside class="abs ad" style="left:553px;top:435px">
  <div class="ad-head">Sponsored links</div>
  <div class="ad-item"><b>Starvale, Novalux, &amp; More</b><br>Premier US Starvale &amp; Novalux Dealer 25 years of friendly expert service<s>www.starvale-shop.example</s></div>
  <div class="ad-item"><b>SkyPoint scope upgrade</b><br>SV200 Classic, SkyDrive, Twinstar No software - just plug &amp; play<s>www.skypoint-eng.example</s></div>
  <div class="ad-item"><b>GPS for Starvale Telescopes</b><br>Add GPS to your SV-ET or SVX55 Scope Fully Integrated Unit - Only $169!<s>www.scopelinker.example</s></div>
  <div class="ad-item"><b>Free Telescope Catalog</b><br>Special low prices on telescopes at Polaris Optics' authoritative website<s>www.polaris-optics.example</s></div>
</aside>
<aside class="abs ad" style="left:553px;top:627px">
  <div class="ad-head">Sponsored links</div>
  <div class="ad-item"><b>Starvale, Novalux, &amp; More</b><br>Premier US Starvale &amp; Novalux Dealer 25 years of friendly expert service<s>www.starvale-shop.example</s></div>
  <div class="ad-item"><b>SkyPoint scope upgrade</b><br>SV200 Classic, SkyDrive, Twinstar No software - just plug &amp; play<s>www.skypoint-eng.example</s></div>
  <div class="ad-item"><b>GPS for Starvale Telescopes</b><br>Add GPS to your SV-ET or SVX55 Scope Fully Integrated Unit - Only $169!<s>www.scopelinker.example</s></div>
  <div class="ad-item"><b>Free Telescope Catalog</b><br>Special low prices on telescopes at Polaris Optics' authoritative website<s>www.polaris-optics.example</s></div>
</aside>

<footer class="abs footer">
  <div class="fcol" style="left:55px"><h4>SPECIALTIES</h4><div class="on">Chiropractors</div>Dentists<br>Dermatologists<br>Eye Doctors<br>Gynecologists<br>Primary Care Doctors<br>Psychiatrists</div>
  <div class="fcol" style="left:199px"><h4>SEARCH BY</h4>Doctor Name<br>Specialty<br>Language<br>Location<br>Hospital<br>Insurance</div>
  <div class="fcol" style="left:344px"><h4>CITIES</h4>Chicago<br>Houston<br>New York<br>Philadelphia<br>Phoenix<br>San Antonio</div>
  <div class="fcol" style="left:488px"><h4>DR. LUMORA</h4>About Us<br>Privacy Policy<br>Temrs of Use<br>Contact<br>Simplified</div>
  <div class="fcol social" style="left:632px"><h4>FOLLOW US</h4><span><i></i>Friendbook</span><span><i></i>Chirper</span><span><i></i>Circles +</span><span><i></i>Linkwork</span></div>
</footer>
<svg class="abs totop" width="44" height="58" viewBox="0 0 44 58" aria-label="Back to top">
  <path d="M22 2C11 2 3 10 3 20c0 12 19 28 19 28s19-16 19-28C41 10 33 2 22 2z" fill="#0a79c2"/>
  <path d="M14 22l8-8 8 8M14 28l8-8 8 8" stroke="#fff" stroke-width="2" fill="none"/>
  <ellipse cx="22" cy="51" rx="12" ry="3.5" fill="none" stroke="#0a79c2" stroke-width="2"/>
</svg>
<div class="abs copy">© <em>DR. LUMORA</em> - 2016. All Rights Reserved</div>

</body>
</html>
```